Wendlemoor Contracting In need of monthly newsletter

We need a monthly newsletter to promote our monthly special of Mulch Installation.

Please change wording to fit what you feel is professional and effective.

Our regular price to install Mulch is $169/Yard installed/Delivered

We would like to run a promotion of $125/Yard Installed & Delivered

Compare us to others $135/Yard Delivered only from some other suppliers

Also list somewhere on the newsletter :
- Delivery of soils, stone, wood also available
- Check out our website
- an emphasis on quality

The Fine Print
* Some Conditions apply
Mulches included in sale Dusk Velvet, Chocolate Brown, Auburn Red, Natural, Hemlock, Gold, Shredded Pine. Some site conditions may incur extra cost. minimum 3 Yards for sale price to be in effect, HST extra on all prices listed,

CHECK OUR WEBSITE FOR SOME IMAGES AND MORE INFORMATION....

ASK ANYTHING YOU WANT VIA Pixel Bazaar

Types of Mulch have changed Slightly in the "Fine Print"

Classic Cedar, Black Cedar, Red Cedar, Chocolate brown, Pine Bark, Natural Shredded Pine, Hemlock, Utility Style.

We will also be submitting pictures of the mulch HOWEVER you might need to crop or alter these images to make them work for our newsletter.

Reason: We have not yet found a design we think is Straight to the point. Simple and with our theme.

```html
<!DOCTYPE html>
<html lang="en">
<head>
<meta charset="utf-8">
<title>Mulch Installation Special Month – Wendlemoor Contracting</title>
<link rel="stylesheet" href="https://fonts.googleapis.com/css2?family=Open+Sans:ital,wght@0,400;0,700;0,800;1,400&family=Mulish:wght@300;400&display=swap">
<style>
  :root {
    --page-bg: #e4e4e4;
    --green-deep: #0a4f1e;
    --green-mid: #158a34;
    --green-bright: #27b04a;
    --glow: rgba(220, 255, 225, 0.45);
    --white: #ffffff;
    --soft-white: #e9f3ea;
    --rule: rgba(255, 255, 255, 0.7);
    --badge: #dfe6e0;
    --photo-brown: #6b4a33;
    --photo-brown-dark: #4a3324;
    --photo-olive: #5e6a3a;
    --photo-green: #3b5e30;
  }
  * { margin: 0; padding: 0; box-sizing: border-box; }
  html, body {
    width: 1200px; height: 1000px; overflow: hidden;
    background: var(--page-bg);
  }
  .flyer {
    position: absolute; left: 80px; top: 110px;
    width: 1040px; height: 780px; overflow: hidden;
    font-family: "Open Sans", Arial, sans-serif; color: var(--white);
    background:
      radial-gradient(ellipse 220px 100px at 82% 18%, var(--glow), transparent 70%),
      radial-gradient(ellipse 900px 520px at 55% 35%, var(--green-bright), transparent 75%),
      linear-gradient(180deg, var(--green-mid) 0%, var(--green-deep) 100%);
  }
  .flyer__title {
    position: absolute; top: 38px; left: 0; width: 100%;
    text-align: center; font-weight: 800; font-size: 34px;
    letter-spacing: 1px; text-shadow: 0 2px 4px rgba(0,0,0,.35);
  }
  .gallery { position: absolute; top: 100px; left: 263px; display: flex; gap: 15px; }
  .gallery__photo {
    width: 120px; height: 120px; border-radius: 50%;
    box-shadow: 0 3px 8px rgba(0,0,0,.35);
  }
  .gallery__photo--bark { background: linear-gradient(160deg, var(--photo-brown), var(--photo-brown-dark)); }
  .gallery__photo--hands { background: linear-gradient(160deg, var(--photo-brown-dark), #3a281c); }
  .gallery__photo--bed { background: linear-gradient(160deg, var(--photo-olive), var(--photo-brown-dark)); }
  .gallery__photo--shrubs { background: linear-gradient(160deg, var(--photo-green), #2f3f25); }

  .price { position: absolute; top: 215px; left: 138px; font-weight: 700; line-height: 1; }
  .price__amount { font-size: 232px; letter-spacing: -6px; text-shadow: 0 4px 10px rgba(0,0,0,.35); }
  .price__cents { position: absolute; top: 78px; left: 388px; font-size: 40px; }
  .price__rule { position: absolute; left: 600px; top: 320px; width: 2px; height: 165px; background: var(--rule); }
  .offer { position: absolute; left: 625px; top: 350px; font-family: "Mulish", Arial, sans-serif; }
  .offer__label { font-weight: 300; font-size: 50px; line-height: 1.02; color: var(--soft-white); }
  .offer__regular { margin-top: 8px; font-size: 13px; font-family: "Open Sans", Arial, sans-serif; color: var(--soft-white); }

  .compare {
    position: absolute; top: 498px; left: 180px; width: 520px;
    text-align: center; font-weight: 700; font-size: 18px; line-height: 1.5;
  }
  .compare__phone { margin-top: 14px; font-size: 36px; font-weight: 800; letter-spacing: 1px; }

  .footer { position: absolute; left: 48px; top: 690px; display: flex; align-items: center; gap: 14px; }
  .badge { display: block; background: var(--badge); border-radius: 3px; }
  .badge--listing { width: 62px; height: 34px; }
  .badge--card { width: 38px; height: 24px; }
  .brand { display: flex; align-items: center; gap: 8px; margin-left: 22px; }
  .brand__dot { width: 26px; height: 26px; border-radius: 50%; background: var(--white); }
  .brand__name { font-weight: 700; font-size: 16px; }
  .contact { position: absolute; left: 48px; top: 736px; font-size: 13px; line-height: 1.4; color: var(--soft-white); }
  .fine-print {
    position: absolute; left: 580px; top: 690px; width: 420px;
    font-style: italic; font-size: 12px; line-height: 1.45; color: var(--soft-white);
  }
</style>
</head>
<body>
  <main class="flyer">
    <h1 class="flyer__title">MULCH INSTALLATION SPECIAL MONTH</h1>

    <div class="gallery">
      <div class="gallery__photo gallery__photo--bark" role="img" aria-label="Photo: mulch spread at the base of a tree"></div>
      <div class="gallery__photo gallery__photo--hands" role="img" aria-label="Photo: handful of dark mulch"></div>
      <div class="gallery__photo gallery__photo--bed" role="img" aria-label="Photo: garden bed with fresh mulch"></div>
      <div class="gallery__photo gallery__photo--shrubs" role="img" aria-label="Photo: landscaped shrubs in mulch"></div>
    </div>

    <div class="price">
      <span class="price__amount">125</span>
      <span class="price__cents">,00</span>
    </div>
    <div class="price__rule"></div>
    <div class="offer">
      <p class="offer__label">Yard Installed<br>&amp; Delivered</p>
      <p class="offer__regular">Regular price is $169. Yard installed &amp; Delivered</p>
    </div>

    <div class="compare">
      <p>Compare us to others</p>
      <p>$135 Yard Delivered only from some other suppliers</p>
      <p>Delivery of soils, stone, wood also available!</p>
      <p class="compare__phone">555.204.7718</p>
    </div>

    <div class="footer">
      <span class="badge badge--listing"></span>
      <span class="badge badge--card"></span>
      <span class="badge badge--card"></span>
      <div class="brand">
        <span class="brand__dot"></span>
        <span class="brand__name">Wendlemoor Contracting</span>
      </div>
    </div>
    <div class="contact">
      <p>info@wendlemoorcontracting.com</p>
      <p>www.wendlemoorcontracting.com</p>
    </div>

    <p class="fine-print">Mulches included in sale Dusk Velvet, Chocolate Brown, Auburn Red, Natural, Hemlock, Gold, Shredded Pine. Some site conditions may incur extra cost. minimum 3 Yards for sale price to be in effect. HST extra on all prices listed.</p>
  </main>
</body>
</html>
```